The Bright Lantern, an online college fair for non-traditional students, needs a web site

I need design and coding for a functioning web site that will serve as an online college fair that connects non-traditional students with college admissions officers and college advisors. I have chosen Wordpress and the "Meridian" theme for the site, and you can see what I already have here: https://brightlanternhub.example/
I need help setting up the site's pages and functionality, including SEO optimization and a password protected area. I will manage all content. In addition to me as the administrator, other users will be: college admissions officers, non-traditional students (like homeschoolers), and college advisors.
Target Market(s)
Homeschoolers and college/university admissions officers
Industry/Entity Type
College
Coding
Coded - Design and coding required
Number of Pages Required
5+ page
Font styles to use
Requirements
Must have
- - An inviting but professional look (see the logo as a starting point)
- - Easy to navigate
- - A way to register subscribed members (students)
- - A password-protected "members only" area
- - Virtual "booths" on the Schools page that lead to a detail page for each school
- - SEO optimized
Nice to have
- - Searchable site

```html
<!DOCTYPE html>
<html lang="en">
<head>
<meta charset="utf-8">
<title>The Bright Lantern</title>
<link href="https://fonts.googleapis.com/css2?family=Open+Sans:wght@300;400;600;700&display=swap" rel="stylesheet">
<style>
:root{
  --stage:#000000;
  --paper:#ffffff;
  --red:#f20a0a;
  --red-soft:#f77b7b;
  --ink:#333333;
  --muted:#555555;
  --dark:#1c1c1c;
  --line:#7a7a7a;
}
*{margin:0;padding:0;box-sizing:border-box}
html,body{width:1200px;height:1119px;overflow:hidden;background:var(--stage)}
body{font-family:"Open Sans",sans-serif;color:var(--ink)}
.site{position:absolute;left:398px;top:0;width:402px;height:1119px;background:var(--paper);overflow:hidden}
.abs{position:absolute}

/* header */
.brand{left:33px;top:13px;display:flex;align-items:center;gap:4px}
.brand-mark{width:22px;height:22px;background:var(--red)}
.brand-name{font-size:7px;font-weight:600;color:var(--ink);letter-spacing:.2px}
.main-nav{left:209px;top:25px;display:flex;gap:5px;font-size:3.6px;color:var(--muted);text-transform:uppercase;list-style:none}

/* hero */
.hero{left:0;top:49px;width:402px;height:229px;background:linear-gradient(120deg,#6d6f86 0%,#4a4a5c 35%,#8a7a78 65%,#c9b8a8 100%)}
.hero-curve{left:0;top:49px}
.hero-welcome{left:164px;top:157px;width:73px;height:17px;background:#222;color:#fff;font-size:9px;font-weight:600;text-align:center;line-height:17px}
.hero-title{left:96px;top:178px;width:209px;height:21px;background:var(--red);color:#fff;font-size:15.5px;font-weight:600;text-align:center;line-height:21px;letter-spacing:.3px}
.hero-arrow{top:170px}

/* newsletter */
.newsletter{left:0;top:278px;width:402px;height:113px;background:var(--red);color:#fff;text-align:center}
.newsletter h2{position:absolute;left:0;right:0;top:20px;font-size:15px;font-weight:300;letter-spacing:.3px}
.newsletter p{position:absolute;left:100px;right:100px;top:48px;font-size:3.8px;line-height:8px}
.news-input{left:121px;top:72px;width:135px;height:18px;background:var(--red-soft);font-size:4px;color:#fff;text-align:left;padding-left:9px;line-height:18px}
.news-button{left:256px;top:72px;width:24px;height:18px;background:#2a2a2a;display:flex;align-items:center;justify-content:center}

/* intro */
.intro-title{left:0;right:0;top:426px;text-align:center;font-size:15px;font-weight:300;color:var(--ink)}
.accent{color:var(--red)}
.intro-text{left:45px;right:45px;top:455px;text-align:center;font-size:3.8px;line-height:8.5px;color:var(--muted)}

/* audience rows */
.feature-title{font-size:9px;font-weight:300;color:var(--ink);line-height:11px;text-transform:uppercase}
.feature-text{font-size:3.8px;line-height:8.8px;color:var(--muted)}
.photo{}

/* contact */
.contact{left:0;top:839px;width:402px;height:209px;background:linear-gradient(90deg,#3a2f26 0%,#2a211a 40%,#151515 70%,#111 100%)}
.contact-title{left:240px;top:866px;font-size:15px;font-weight:300;color:#fff}
.field{left:214px;width:146px;border:1px solid var(--line);font-size:4px;color:#aaa;padding:4px 6px}
.submit{left:302px;top:1015px;width:58px;height:15px;background:var(--red);color:#fff;font-size:4.5px;font-weight:700;text-align:center;line-height:15px}

/* call band */
.call-band{left:0;top:1048px;width:402px;height:54px;background:var(--red);color:#fff}
.phone{left:61px;top:1056px;font-size:29px;font-weight:700;color:#fff;letter-spacing:.5px}
.contact-line{left:265px;font-size:6.5px;color:#fff;display:flex;gap:4px;align-items:flex-start;line-height:6.5px}

/* footer */
.copyright{left:27px;top:1107px;font-size:3.8px;color:var(--muted)}
.social{left:340px;top:1106px;display:flex;gap:4px}
.social span{width:7px;height:7px;display:block}
</style>
</head>
<body>
<div class="site">

  <header>
    <div class="abs brand"><span class="brand-mark"></span><span class="brand-name">THE BRIGHT LANTERN</span></div>
    <ul class="abs main-nav">
      <li>Home</li><li>Students</li><li>Schools</li><li>Advisors</li><li>Member Resources</li><li>News</li><li>Contact Us</li>
    </ul>
  </header>

  <div class="abs hero" role="img" aria-label="Photo of a student with a mug working on a laptop at a desk"></div>
  <svg class="abs hero-curve" width="402" height="30" viewBox="0 0 402 30" aria-hidden="true">
    <path d="M0 0 H402 V30 Q300 0 201 0 Q100 0 0 30 Z" fill="#ffffff"/>
  </svg>
  <svg class="abs hero-arrow" style="left:12px" width="8" height="16" viewBox="0 0 8 16"><path d="M7 1 L1 8 L7 15" stroke="#fff" stroke-width="1" fill="none"/></svg>
  <svg class="abs hero-arrow" style="left:382px" width="8" height="16" viewBox="0 0 8 16"><path d="M1 1 L7 8 L1 15" stroke="#fff" stroke-width="1" fill="none"/></svg>
  <div class="abs hero-welcome">Welcome To</div>
  <div class="abs hero-title">BRIGHT LANTERN</div>

  <section class="abs newsletter">
    <h2>NEWSLETTER</h2>
    <p>Get fair dates, school news and admissions tips sent to your inbox. Join our list today and never miss an open booth or a live panel again.</p>
    <div class="abs news-input">Email</div>
    <div class="abs news-button">
      <svg width="9" height="9" viewBox="0 0 10 10"><path d="M1 5 L9 1 L6 9 L5 5.5 Z" stroke="#fff" stroke-width=".7" fill="none"/></svg>
    </div>
  </section>

  <h2 class="abs intro-title">BRIGHT <span class="accent">LANTERN</span></h2>
  <p class="abs intro-text">An online college fair that connects non-traditional students with admissions officers and independent advisors. Explore schools, ask questions and plan your path to college from home, at your own pace.</p>

  <h3 class="abs feature-title" style="left:31px;top:508px">For <span class="accent">Students</span></h3>
  <p class="abs feature-text" style="left:31px;top:522px;width:160px">Free membership for any student or parent who wants to learn more about colleges that actively recruit non-traditional students. In one place you will have access to admissions officers, independent advisors, regular articles on higher education topics, resource reviews and links. We also host events, webinars and admissions panels where you can talk directly with officers and advisors.</p>
  <div class="abs photo" style="left:202px;top:497px;width:200px;height:114px;background:linear-gradient(135deg,#b9c3cf,#7d8a9c 50%,#d8dde3)" role="img" aria-label="Photo of students and a mentor talking around a meeting table"></div>

  <div class="abs photo" style="left:0;top:611px;width:201px;height:115px;background:linear-gradient(135deg,#d9dde2,#8d8f93 45%,#2e3036 80%,#e6e6e6)" role="img" aria-label="Photo of admissions officers in a business meeting"></div>
  <h3 class="abs feature-title" style="left:215px;top:632px">For Colleges <span class="accent">and Universities</span></h3>
  <p class="abs feature-text" style="left:215px;top:650px;width:160px">An audience of thousands of non-traditional students who want to hear about your school. You get a dedicated page for a virtual booth where you can describe your institution, highlight programs, share admissions steps and give contact details.</p>

  <h3 class="abs feature-title" style="left:31px;top:748px">For Independent <span class="accent">College<br>Advisors</span></h3>
  <p class="abs feature-text" style="left:31px;top:774px;width:160px">A platform for sharing your services and connecting with thousands of students who need guidance. Through forums, articles and online events you can share your knowledge and work closely with students.</p>
  <div class="abs photo" style="left:202px;top:726px;width:200px;height:113px;background:linear-gradient(135deg,#2a2c33,#4b4f5a 45%,#c9b9a8 75%,#ece7e1)" role="img" aria-label="Photo of advisors reviewing work on a laptop"></div>

  <section class="abs contact" role="img" aria-label="Photo of a student with headphones studying at a laptop"></section>
  <h2 class="abs contact-title">CONTACT US</h2>
  <div class="abs field" style="top:893px;height:17px">Name</div>
  <div class="abs field" style="top:915px;height:17px">Subject</div>
  <div class="abs field" style="top:936px;height:17px">Email</div>
  <div class="abs field" style="top:958px;height:53px">Comments</div>
  <div class="abs submit">SUBMIT</div>

  <div class="abs call-band"></div>
  <div class="abs phone">555 014 2290</div>
  <div class="abs contact-line" style="top:1063px">
    <svg width="7" height="6" viewBox="0 0 7 6"><rect x=".4" y=".4" width="6.2" height="5.2" fill="none" stroke="#fff" stroke-width=".6"/><path d="M.4 .4 L3.5 3 L6.6 .4" fill="none" stroke="#fff" stroke-width=".6"/></svg>
    <span>hello@brightlantern.example</span>
  </div>
  <div class="abs contact-line" style="top:1075px">
    <svg width="6" height="8" viewBox="0 0 6 8"><path d="M3 7.6 C1 5 .4 4 .4 3 A2.6 2.6 0 0 1 5.6 3 C5.6 4 5 5 3 7.6 Z" fill="none" stroke="#fff" stroke-width=".6"/><circle cx="3" cy="3" r=".9" fill="#fff"/></svg>
    <span>410 harbor view lane<br>seaside, CA 90000</span>
  </div>

  <footer>
    <p class="abs copyright">Copyright © 2017 Bright Lantern. All rights reserved</p>
    <div class="abs social">
      <span style="background:#f2a33a"></span>
      <span style="background:#3aa3e3"></span>
      <span style="background:#d6457b"></span>
      <span style="background:#36b3d1"></span>
      <span style="background:#3b5998"></span>
    </div>
  </footer>

</div>
</body>
</html>
```